Book cover design for a debut author; 'Quiet Ashes' by Bram Holloway.

My father has written a book and I would love to gift him a bespoke front cover for it for his 60th birthday this year.
The book is a work of fiction and tells the story of two strangers (an Asian Female and a Caucasian Male) who meet on a train. After the train crashes and bursts into flames, they take the luggage of different passengers and decide to make a new life together, culminating in a murder which they believe they can get away with forever. The book is a thriller and engages the reader in suspense, excitement, anticipation and anxiety.

Target Market(s)

Thriller Fiction Readers

Font styles to use
Serif

Colors

Designer to choose colors to be used in the design.

Requirements
Must have
• A vibrant front cover with consideration over the font of both the title and author.
• I would like the train where they meet to be the main focus for the front cover. The strangers meet on a train and I’d like the cover to reflect this.
• Design must include front cover, spine and back cover with a space for blurb (to follow).
Nice to have
• A photograph based cover would I think suit the book better than an illustration.

```html
<!DOCTYPE html>
<html lang="en">
<head>
<meta charset="utf-8">
<title>Quiet Ashes — Cover Spread</title>
<link href="https://fonts.googleapis.com/css2?family=Montserrat:wght@500;600;700;800&display=swap" rel="stylesheet">
<style>
  :root {
    --bg: #e4e4e4;
    --rust: #962a1f;
    --ink: #0b0b0b;
    --panel: #1a1a1a;
    --paper: #ffffff;
    --ember: #f08a1e;
    --ember-dark: #5a1a0e;
  }
  * { box-sizing: border-box; margin: 0; padding: 0; }
  html, body { width: 1200px; height: 1000px; overflow: hidden; }
  body {
    background: var(--bg);
    font-family: "Montserrat", sans-serif;
    display: flex; align-items: center; justify-content: center;
  }
  .cover-spread {
    display: flex; height: 720px;
    box-shadow: 0 20px 40px rgba(0,0,0,0.18);
  }
  /* Back cover */
  .back-cover {
    width: 470px; background: var(--ink); position: relative;
    display: flex; flex-direction: column;
  }
  .back-cover__band {
    background: var(--rust); color: var(--paper);
    padding: 40px 40px 34px; text-align: center;
    font-weight: 800; font-size: 19px; letter-spacing: 4px; line-height: 1.45;
  }
  .back-cover__blurb {
    color: var(--paper); padding: 34px 44px 0; text-align: center;
    font-weight: 500; font-size: 17px; letter-spacing: 2.5px; line-height: 1.55;
  }
  .back-cover__blurb-box {
    margin: 24px 36px 0; background: var(--panel); border-radius: 10px;
    padding: 22px 20px; color: var(--paper); text-align: center;
    font-weight: 500; font-size: 16px; letter-spacing: 2.5px; line-height: 1.55;
  }
  .back-cover__flames {
    position: absolute; left: 0; right: 0; bottom: 0; height: 120px;
    background: linear-gradient(to top, #f2a23a 0%, #c24a12 35%, rgba(60,15,5,0.6) 70%, rgba(11,11,11,0) 100%);
  }
  /* Spine */
  .spine {
    width: 70px; background: var(--rust); position: relative;
    display: flex; align-items: center; justify-content: center;
  }
  .spine__text {
    writing-mode: vertical-rl; color: var(--paper);
    display: flex; align-items: center; gap: 18px;
    font-weight: 700; letter-spacing: 3px; white-space: nowrap;
  }
  .spine__title { font-size: 34px; font-weight: 600; }
  .spine__author { font-size: 22px; }
  .spine__divider { width: 2px; height: 60px; background: var(--paper); writing-mode: horizontal-tb; }
  /* Front cover */
  .front-cover { width: 470px; position: relative; overflow: hidden; }
  .front-cover__photo {
    position: absolute; inset: 0;
    background:
      radial-gradient(ellipse at 78% 62%, #ffd36a 0%, #f08a1e 18%, rgba(200,70,20,0.75) 38%, rgba(0,0,0,0) 62%),
      radial-gradient(ellipse at 40% 30%, rgba(240,120,30,0.55) 0%, rgba(0,0,0,0) 55%),
      linear-gradient(to bottom, #3b1a12 0%, #6a2c18 35%, #4a3a34 60%, #2a2422 80%, #1a1412 100%);
  }
  .front-cover__flames {
    position: absolute; left: 0; right: 0; bottom: 0; height: 150px;
    background: linear-gradient(to top, #f7b548 0%, #e06a18 40%, rgba(140,40,10,0.4) 75%, rgba(0,0,0,0) 100%);
  }
  .front-cover__title {
    position: absolute; top: 60px; left: 0; right: 0; text-align: center;
    color: var(--paper); font-weight: 700; font-size: 82px; line-height: 0.98;
    letter-spacing: 6px;
  }
  .front-cover__credit {
    position: absolute; bottom: 70px; left: 0; right: 0; text-align: center;
  }
  .front-cover__label {
    color: var(--paper); font-weight: 500; font-size: 26px; letter-spacing: 4px;
  }
  .front-cover__author {
    color: var(--ink); font-weight: 800; font-size: 34px; letter-spacing: 3px; margin-top: 2px;
  }
</style>
</head>
<body>
  <main class="cover-spread">
    <section class="back-cover">
      <h2 class="back-cover__band">THE RIVETING<br>FICTIONAL<br>STORY OF TWO<br>STRANGERS WHO<br>MEET ON A TRAIN</h2>
      <p class="back-cover__blurb">After the train bursts into flames, they take the luggage of different passengers to make a new life together,</p>
      <p class="back-cover__blurb-box">culminating in a murder they believe they can get away with forever. A gripping and engaging thriller of suspense, excitement and anxiety.</p>
      <div class="back-cover__flames" role="img" aria-label="Photograph of flames along the bottom edge"></div>
    </section>

    <section class="spine">
      <div class="spine__text">
        <span class="spine__author">BRAM HOLLOWAY</span>
        <span class="spine__divider"></span>
        <span class="spine__title">QUIET ASHES</span>
      </div>
    </section>

    <section class="front-cover">
      <div class="front-cover__photo" role="img" aria-label="Photograph of a passenger train carriage engulfed in flames at a station platform"></div>
      <div class="front-cover__flames" role="img" aria-label="Photograph of flames along the bottom edge"></div>
      <h1 class="front-cover__title">QUIET<br>ASHES</h1>
      <div class="front-cover__credit">
        <p class="front-cover__label">DEBUT AUTHOR</p>
        <p class="front-cover__author">BRAM HOLLOWAY</p>
      </div>
    </section>
  </main>
</body>
</html>
```